Desk Allies Business Card

Contact Information for Business Card

Janne Voutilainen
Managing Director

3/47 Brindle Street Harlow ACT 2915

Tel: +61 02 6257 3140
Mob: +61 0427 315 846

Email: janne@deskallies.com.au
Web: www.deskallies.com.au

Colors

Designer to choose colors to be used in the design.

Requirements
Must have
• Logo, Name, Title, Address, Telephone, Mobile, Email Address and Website
• "Desk Ally International Pty Ltd"

```html
<!DOCTYPE html>
<html lang="en">
<head>
<meta charset="utf-8">
<title>Desk Allies Business Card</title>
<link href="https://fonts.googleapis.com/css2?family=Lato:wght@400;700&family=Montserrat:wght@400;500&display=swap" rel="stylesheet">
<style>
  :root {
    --backdrop: #1c1c1d;
    --card-dark: #2a2a2c;
    --card-light: #ffffff;
    --brand-blue: #1b7fc9;
    --silver: #b9b9bd;
    --muted: #77777b;
    --ink: #111112;
    --text-light: #f2f2f2;
  }
  * { margin: 0; padding: 0; box-sizing: border-box; }
  html, body { width: 1200px; height: 900px; overflow: hidden; }
  body {
    background: var(--backdrop);
    font-family: "Lato", sans-serif;
    position: relative;
  }
  .card {
    position: absolute;
    left: 280px;
    width: 640px;
    height: 366px;
    border-radius: 14px;
    overflow: hidden;
    box-shadow: 0 14px 34px rgba(0,0,0,.55);
  }
  /* Front */
  .card-front { top: 56px; background: var(--card-dark); }
  .front-brand {
    position: absolute; left: 96px; top: 118px;
    display: flex; align-items: center; gap: 22px;
  }
  .brand-dot {
    width: 74px; height: 74px; border-radius: 50%;
    background: var(--ink);
    flex: none;
  }
  .front-wordmark {
    font-family: "Montserrat", sans-serif;
    font-weight: 500;
    font-size: 46px;
    letter-spacing: 2px;
    color: var(--silver);
    line-height: 1;
  }
  .front-tagline {
    font-family: "Montserrat", sans-serif;
    font-weight: 400;
    font-size: 13px;
    letter-spacing: 5.2px;
    color: var(--muted);
    margin-top: 10px;
    white-space: nowrap;
  }
  .front-url {
    position: absolute; left: 0; right: 0; bottom: 52px;
    text-align: center;
    font-family: "Montserrat", sans-serif;
    font-size: 15px; letter-spacing: 5px;
    color: var(--ink);
    font-weight: 500;
  }
  /* Back */
  .card-back { top: 478px; background: var(--card-dark); }
  .back-panel {
    position: absolute; left: 0; top: 0; bottom: 0; width: 232px;
    background: var(--card-light);
    display: flex; flex-direction: column; align-items: center; justify-content: center; gap: 16px;
  }
  .panel-dot {
    width: 70px; height: 70px; border-radius: 50%;
    border: 12px solid var(--brand-blue);
  }
  .panel-name {
    font-family: "Lato", sans-serif; font-weight: 700;
    font-size: 26px; color: var(--brand-blue); letter-spacing: 1px;
  }
  .divider {
    position: absolute; top: 0; bottom: 0; left: 232px; width: 26px;
    background: linear-gradient(90deg,
      var(--ink) 0 5px, var(--card-light) 5px 8px,
      var(--ink) 8px 13px, var(--card-light) 13px 16px,
      var(--ink) 16px 21px, var(--card-dark) 21px);
  }
  .back-details { position: absolute; left: 300px; top: 42px; right: 30px; color: var(--text-light); }
  .person-name {
    font-weight: 700; font-size: 22px; color: var(--brand-blue);
    text-transform: uppercase; letter-spacing: .5px;
  }
  .person-title { font-size: 14px; margin-top: 2px; }
  .contact-list { list-style: none; margin-top: 58px; }
  .contact-list li {
    display: flex; align-items: center; gap: 14px;
    font-size: 15px; line-height: 27px;
  }
  .contact-list svg { width: 14px; height: 14px; fill: var(--brand-blue); flex: none; }
  .company-name {
    margin-top: 26px; font-weight: 700; font-size: 14px;
    color: var(--brand-blue); text-transform: uppercase;
    text-decoration: underline; text-underline-offset: 3px;
  }
  .company-address { font-weight: 700; font-size: 14px; margin-top: 6px; }
</style>
</head>
<body>
  <section class="card card-front">
    <div class="front-brand">
      <div class="brand-dot"></div>
      <div>
        <div class="front-wordmark">DESK ALLIES</div>
        <div class="front-tagline">HEALTHY WORKSPACE SOLUTIONS</div>
      </div>
    </div>
    <div class="front-url">www.deskallies.com.au</div>
  </section>

  <section class="card card-back">
    <div class="back-panel">
      <div class="panel-dot"></div>
      <div class="panel-name">Desk Allies</div>
    </div>
    <div class="divider"></div>
    <div class="back-details">
      <div class="person-name">Janne Voutilainen</div>
      <div class="person-title">Managing Director</div>
      <ul class="contact-list">
        <li>
          <svg viewBox="0 0 16 16"><path d="M3 1l3 3-2 2c1 2 3 4 5 5l2-2 3 3-2 3C7 15 1 9 1 3z"/></svg>
          +61 02 6257 3140
        </li>
        <li>
          <svg viewBox="0 0 16 16"><path d="M1 3h14v10H1z M1 3l7 6 7-6" fill="none" stroke="#1b7fc9" stroke-width="2"/></svg>
          +61 0427 315 846
        </li>
        <li>
          <svg viewBox="0 0 16 16"><circle cx="8" cy="8" r="6.5" fill="none" stroke="#1b7fc9" stroke-width="2"/><path d="M1.5 8h13M8 1.5c-3 3.5-3 9.5 0 13M8 1.5c3 3.5 3 9.5 0 13" fill="none" stroke="#1b7fc9" stroke-width="1.4"/></svg>
          janne@deskallies.com.au
        </li>
      </ul>
      <div class="company-name">Desk Ally International Pty Ltd</div>
      <div class="company-address">3/47 Brindle Street Harlow ACT 2915</div>
    </div>
  </section>
</body>
</html>
```